Birchline Cabinets & Countertops Business Cards

We need a new business card design. Pixel Harbor did a great job on our logo design so let's get that business card done. We build custom kitchen and bath cabinets. We also do cabinets for mud rooms, closets, living rooms, bars, etc.
We would like to include a QR code somewhere in addition to our Name, Position, Email, Phone, Cell and Web Site. On the back of the card, we want to use that space to include all the various types of projects we design for. Also I am not sure it would like good or not, but a faint watermark kitchen CAD layout, etc might look cool.
To see the categories or project types we do, visit our website at https://birchlinecabinetsandcounters.example
Just be creative and give us what you got!
Contact Information for Business Card
Name, Position, Phone, Cell Phone, Email, Website, QR Code

```html
<!DOCTYPE html>
<html lang="en">
<head>
<meta charset="utf-8">
<title>Birchline Cabinets &amp; Countertops – Business Card</title>
<link rel="stylesheet" href="https://fonts.googleapis.com/css2?family=Jost:wght@400;500;700&display=swap">
<style>
  :root {
    --backdrop: #5f5f5f;
    --card-base: #ebebe8;
    --navy: #1f3f73;
    --gold: #cbae6c;
    --slate-blue: #9fb3c2;
    --icon-grey: #8fa3b0;
    --white: #ffffff;
  }
  * { margin: 0; padding: 0; box-sizing: border-box; }
  html, body { width: 1200px; height: 1000px; overflow: hidden; }
  body { background: var(--backdrop); font-family: "Jost", sans-serif; position: relative; }

  .card {
    position: absolute; left: 283px; width: 634px; height: 410px;
    border-radius: 30px; overflow: hidden; background: var(--card-base);
    box-shadow: 0 10px 22px rgba(0,0,0,0.35);
  }
  .card-front { top: 63px; }
  .card-back { top: 527px; }

  /* front */
  .kitchen-photo {
    position: absolute; left: 265px; top: 10px; width: 357px; height: 217px;
    border-top-right-radius: 20px;
    background: linear-gradient(180deg, #e4e6e5 0%, #c9cecf 45%, #5c6668 70%, #7a5c45 100%);
  }
  .brand-name {
    position: absolute; color: var(--navy); font-weight: 500;
    text-transform: uppercase; text-align: center; letter-spacing: 1px; line-height: 1.25;
  }
  .card-front .brand-name { left: 30px; top: 150px; width: 230px; font-size: 20px; }
  .name-band { position: absolute; left: 0; top: 227px; width: 100%; height: 68px; background: var(--white); }
  .person-name {
    position: absolute; right: 47px; top: 236px; font-size: 33px; font-weight: 700;
    color: var(--navy); letter-spacing: 1px; line-height: 1;
  }
  .person-role {
    position: absolute; right: 47px; top: 270px; font-size: 14px; letter-spacing: 3px;
    color: var(--gold); line-height: 1;
  }
  .gold-rule { position: absolute; left: 0; top: 301px; width: 100%; height: 15px; background: var(--gold); }
  .contact {
    position: absolute; right: 74px; top: 326px; text-align: right;
    color: var(--navy); font-size: 14px; line-height: 16px; letter-spacing: 0.4px;
  }
  .contact-icon { position: absolute; right: 50px; }
  .qr-code {
    position: absolute; left: 28px; top: 326px; width: 66px; height: 66px;
    background: var(--white); border: 2px solid var(--navy); border-radius: 4px;
  }
  .online {
    position: absolute; left: 104px; top: 342px;
    color: var(--navy); font-size: 12.5px; line-height: 17px; letter-spacing: 0.3px;
  }

  /* back */
  .back-photo {
    position: absolute; inset: 0 0 auto 0; height: 152px;
    background: linear-gradient(180deg, #e9eae7, #dcdedb);
  }
  .back-gold { position: absolute; left: 0; top: 152px; width: 100%; height: 106px; background: var(--gold); }
  .back-slate { position: absolute; left: 0; top: 258px; width: 100%; height: 152px; background: var(--slate-blue); }
  .logo-panel {
    position: absolute; left: 179px; top: 106px; width: 276px; height: 197px;
    background: var(--white); border-radius: 28px;
  }
  .card-back .brand-name { left: 0; top: 70px; width: 276px; font-size: 21px; }
  .project-types {
    position: absolute; left: 0; top: 322px; width: 100%; text-align: center;
    color: var(--white); font-size: 14px; font-weight: 500; letter-spacing: 2px;
    line-height: 24px; text-transform: uppercase;
  }
</style>
</head>
<body>

<section class="card card-front">
  <div class="kitchen-photo" role="img" aria-label="Photo of a bright kitchen with a grey island and wood beams"></div>
  <div class="brand-name">Birchline Cabinets<br>&amp; Countertops</div>
  <div class="name-band"></div>
  <div class="person-name">YOUR NAME</div>
  <div class="person-role">DIRECTOR</div>
  <div class="gold-rule"></div>

  <div class="qr-code" role="img" aria-label="QR code linking to the company website"></div>
  <div class="online">
    info@birchlinecabinetsandcounters.example<br>
    birchlinecabinetsandcounters.example
  </div>

  <div class="contact">
    4471 Harborline Ave, Suite 210-B,<br>
    Seaview Bay, FL 32999<br>
    Office (555) 014-2870<br>
    Cell (555) 014-2871
  </div>
  <svg class="contact-icon" style="top:324px" width="18" height="22" viewBox="0 0 18 22" aria-hidden="true">
    <path d="M9 1a7 7 0 0 0-7 7c0 5 7 12 7 12s7-7 7-12a7 7 0 0 0-7-7z" fill="none" stroke="var(--icon-grey)" stroke-width="2"/>
    <circle cx="9" cy="8" r="2.5" fill="var(--icon-grey)"/>
  </svg>
  <svg class="contact-icon" style="top:358px" width="18" height="18" viewBox="0 0 18 18" aria-hidden="true">
    <path d="M4 1l3 4-2 2c1 3 3 5 6 6l2-2 4 3-2 3C8 17 1 10 1 3z" fill="var(--icon-grey)"/>
  </svg>
  <svg class="contact-icon" style="top:373px" width="18" height="18" viewBox="0 0 18 18" aria-hidden="true">
    <rect x="4" y="1" width="10" height="16" rx="2" fill="none" stroke="var(--icon-grey)" stroke-width="2"/>
    <circle cx="9" cy="13.5" r="1.2" fill="var(--icon-grey)"/>
  </svg>
</section>

<section class="card card-back">
  <div class="back-photo" role="img" aria-label="Faint photo of the kitchen with pendant lights"></div>
  <div class="back-gold"></div>
  <div class="back-slate" role="img" aria-label="Faint tinted photo of the kitchen island"></div>
  <div class="logo-panel">
    <div class="brand-name">Birchline Cabinets<br>&amp; Countertops</div>
  </div>
  <div class="project-types">
    Kitchens · Baths · Mud Rooms · Closets<br>
    Living Rooms · Bars · Offices · Laundry
  </div>
</section>

</body>
</html>
```